Fintech company needs ads created around "can't afford help"

Design 3 ads (total) that focus around HELPING people who can't afford to get help with their finances.

The 3 ads will be made up of 1 design for each audience:
• Millennial
• Generation X
• Baby Boomer

We are testing campaigns in Chirpwall that will drive to a landing page. We are an online financial-tech company who helps people manage their retirement account. We’re looking for creative talent who are effective at developing imagery to be used in Chirpwall to grab people’s attention and drive clicks. Because of the scrutiny in our industry, we’ll handle the ad copy above and below the imagery you create. We encourage you to use/not use words in your creative.

Target Market(s)

• Millennial
• Generation X
• Baby Boomer

Industry/Entity Type

Financial Service

Requirements
Must have
• Image Dimensions
• Width: 1200 Height: 628
• Final PSD Designs
• Feel free to play around with any color scheme.
• Tasteful – we are not a traditional, stodgy Linden Row Financial firm, but we need to convey that we are trustworthy and legitimate.
Nice to have
• You are not limited to photos – whatever you believe will stand out and engage with prospective clients is fair game (including illustrations, animation, video, etc).
• Think about how your work could translate into other forms such as motion graphics or video.
• Ultimately, we will test our favorites and come back to those with the highest performance which will turn into additional work and additional formats.
Should not have
• • No stock photography UNLESS found at Pixanta (we will pay for the image)
• • No Testimonials – regulations prevent us from using testimonials in our advertisements

```html
<!DOCTYPE html>
<html lang="en">
<head>
<meta charset="utf-8">
<title>Helping people who can't afford to get help with their finances</title>
<link rel="stylesheet" href="https://fonts.googleapis.com/css2?family=Montserrat:wght@300;400&display=swap">
<style>
  :root {
    --stage: #1a1a1a;
    --paper: #ffffff;
    --ink: #3a3a3a;
    --ink-soft: #6b6b6b;
    --navy: #22303c;
    --green-light: #7cbc0a;
    --green-mid: #66aa00;
    --green-deep: #5a9800;
    --photo-warm: #e9d6c6;
    --photo-light: #f6f3ef;
    --photo-tree: #7c9a6a;
  }
  * { margin: 0; padding: 0; box-sizing: border-box; }
  html, body {
    width: 1200px;
    height: 808px;
    overflow: hidden;
    background: var(--stage);
  }
  .ad {
    position: absolute;
    top: 90px;
    left: 0;
    width: 1200px;
    height: 628px;
    background: var(--paper);
    overflow: hidden;
    font-family: "Montserrat", sans-serif;
  }
  .ad__art {
    position: absolute;
    inset: 0;
    width: 1200px;
    height: 628px;
  }
  .ad__logo {
    position: absolute;
    left: 390px;
    top: 522px;
    width: 200px;
    text-align: center;
    color: var(--paper);
    font-size: 44px;
    font-weight: 400;
    letter-spacing: 1px;
    line-height: 1;
  }
  .ad__headline {
    position: absolute;
    right: 52px;
    top: 222px;
    text-align: right;
    color: var(--ink);
    font-weight: 300;
  }
  .ad__headline-lead {
    display: block;
    font-size: 62px;
    line-height: 66px;
    letter-spacing: 1px;
  }
  .ad__headline-body {
    display: block;
    font-size: 34px;
    line-height: 54px;
    color: var(--ink-soft);
  }
  .ad__headline-close {
    display: block;
    font-size: 62px;
    line-height: 74px;
  }
</style>
</head>
<body>
  <section class="ad">
    <svg class="ad__art" viewBox="0 0 1200 628" xmlns="http://www.w3.org/2000/svg">
      <defs>
        <linearGradient id="photo-tones" x1="0" y1="0" x2="1" y2="0.6">
          <stop offset="0" stop-color="var(--photo-light)"/>
          <stop offset="0.45" stop-color="var(--photo-warm)"/>
          <stop offset="0.8" stop-color="var(--photo-light)"/>
          <stop offset="1" stop-color="var(--photo-tree)"/>
        </linearGradient>
      </defs>
      <polygon class="ad__photo" role="img"
        aria-label="Photo of a smiling family of three looking at a smartphone together, with a decorated tree behind them"
        points="0,0 909,0 281,628 0,628" fill="url(#photo-tones)"/>
      <polygon class="ad__shape ad__shape--green-light" points="598,312 914,628 702,628 490,415" fill="var(--green-light)"/>
      <polygon class="ad__shape ad__shape--green-mid" points="702,420 806,524 702,628 598,524" fill="var(--green-mid)"/>
      <polygon class="ad__shape ad__shape--green-deep" points="806,524 914,628 702,628" fill="var(--green-deep)"/>
      <polygon class="ad__shape ad__shape--navy" points="490,415 702,628 277,628" fill="var(--navy)"/>
    </svg>

    <div class="ad__logo">LOGO</div>

    <h1 class="ad__headline">
      <span class="ad__headline-lead">HELPING</span>
      <span class="ad__headline-body">people who can't afford</span>
      <span class="ad__headline-body">to get help with their</span>
      <span class="ad__headline-close">finances</span>
    </h1>
  </section>
</body>
</html>
```